Ferncrest Dental, LLC business card project

Business card to be designed with current logo.
Dental office- please keep design of card that looks clean and professional.
Please include the following info:
Ferncrest Dental, LLC
Dr. Lorna Pettigrew
2871 Marlowe Street
Larkfield, OR 97321
541-555-0193
ferncrestdental.office@examplemail.test
Hello everyone-
Reason: Just got back from overseas- will look at all designs and provide feedback. Thank you!
Reason: Polling my friends for the final selection-
thank you to all those that participated- so many talented designers!

```html
<!DOCTYPE html>
<html lang="en">
<head>
<meta charset="utf-8">
<title>Ferncrest Dental, LLC — Business Card</title>
<link rel="stylesheet" href="https://fonts.googleapis.com/css2?family=Open+Sans:wght@300;400;700&display=swap">
<style>
  :root {
    --page-bg: #e9eaea;
    --green-dark: #5fa829;
    --green-mid: #8cc43a;
    --green-light: #cfe24a;
    --charcoal: #454545;
    --text-grey: #5a5a5a;
    --brand-green: #8cc43a;
  }
  * { margin: 0; padding: 0; box-sizing: border-box; }
  html, body {
    width: 1200px;
    height: 1022px;
    overflow: hidden;
    background: var(--page-bg);
    font-family: "Open Sans", Arial, sans-serif;
  }
  .sheet { position: relative; width: 1200px; height: 1022px; }
  .card {
    position: absolute;
    left: 250px;
    width: 700px;
    height: 400px;
    border-radius: 20px;
    box-shadow: 0 6px 18px rgba(0,0,0,0.18);
    overflow: hidden;
  }
  .card--front { top: 81px; }
  .card--back { top: 541px; }
  .card svg { display: block; }
  .brand-name { font-weight: 300; fill: var(--brand-green); }
  .brand-name--reverse { fill: #ffffff; }
  .doctor-name { font-weight: 700; fill: var(--green-dark); }
  .contact-line { font-weight: 400; fill: var(--text-grey); }
  .address-line { font-weight: 400; fill: #ffffff; }
</style>
</head>
<body>
<main class="sheet">

  <section class="card card--front" aria-label="Business card front">
    <svg width="700" height="400" viewBox="0 0 700 400" xmlns="http://www.w3.org/2000/svg">
      <defs>
        <linearGradient id="front-paper" x1="0" y1="0" x2="0" y2="1">
          <stop offset="0" stop-color="#ffffff"/>
          <stop offset="1" stop-color="#f0f0f0"/>
        </linearGradient>
        <linearGradient id="front-band" x1="0" y1="0" x2="0" y2="1">
          <stop offset="0" stop-color="#9ccd3c"/>
          <stop offset="1" stop-color="#6bb02c"/>
        </linearGradient>
        <radialGradient id="faint-scene" cx="0.5" cy="0.5" r="0.5">
          <stop offset="0" stop-color="#dfe9c8" stop-opacity="0.8"/>
          <stop offset="1" stop-color="#ffffff" stop-opacity="0"/>
        </radialGradient>
      </defs>

      <rect class="card-paper" width="700" height="400" fill="url(#front-paper)"/>

      <ellipse class="faint-scene" role="img" aria-label="Faint tree and hill background illustration"
               cx="420" cy="200" rx="170" ry="110" fill="url(#faint-scene)"/>

      <path class="footer-charcoal" d="M0,322 H462 C505,322 510,262 556,262 H700 V400 H0 Z" fill="var(--charcoal)"/>
      <path class="footer-green" d="M0,356 H478 C520,356 526,294 572,294 H700 V400 H0 Z" fill="url(#front-band)"/>

      <circle class="brand-dot" cx="52" cy="60" r="9" fill="var(--brand-green)"/>
      <text class="brand-name" x="72" y="74" font-size="40">Ferncrest Dental, LLC</text>

      <text class="doctor-name" x="160" y="150" font-size="27">Dr. Lorna Pettigrew</text>

      <g class="contact-phone">
        <g transform="translate(160,182)" fill="none" stroke="var(--green-mid)" stroke-width="1.6">
          <rect x="0" y="0" width="15" height="13" rx="3"/>
          <path d="M3,5 Q7.5,1 12,5"/>
        </g>
        <text class="contact-line" x="186" y="194" font-size="16">541-555-0193</text>
      </g>
      <g class="contact-email">
        <g transform="translate(160,211)">
          <rect x="0" y="0" width="15" height="12" fill="var(--green-mid)"/>
          <path d="M1,1 L7.5,7 L14,1" fill="none" stroke="#ffffff" stroke-width="1.4"/>
        </g>
        <text class="contact-line" x="186" y="223" font-size="16">ferncrestdental.office@examplemail.test</text>
      </g>

      <text class="address-line" x="18" y="344" font-size="15">2871 Marlowe Street, Larkfield, OR 97321</text>
    </svg>
  </section>

  <section class="card card--back" aria-label="Business card back">
    <svg width="700" height="400" viewBox="0 0 700 400" xmlns="http://www.w3.org/2000/svg">
      <defs>
        <radialGradient id="back-glow" cx="0.5" cy="0.45" r="0.65">
          <stop offset="0" stop-color="#cfe24a"/>
          <stop offset="0.55" stop-color="#8cc43a"/>
          <stop offset="1" stop-color="#5fa829"/>
        </radialGradient>
      </defs>
      <rect width="700" height="400" fill="url(#back-glow)"/>
      <circle class="brand-dot" cx="350" cy="150" r="14" fill="#ffffff"/>
      <text class="brand-name brand-name--reverse" x="350" y="230" font-size="50" text-anchor="middle">Ferncrest Dental, LLC</text>
    </svg>
  </section>

</main>
</body>
</html>
```